Tavenorix - world unique technology for better life - please let them know who am i at first sight

We need a new business card for company which is a provider of unique crystal based technology suitable for all living being. For more information and final design you can use our brochure (our colours are black and blue from brochure).
We use Verdana font

Industry/Entity Type

Business

Contact Information for Business Card

regular dimension

Font styles to use
Other font styles liked:
• Verdana

Requirements
Must have
• Logo
• name
• function/position
• phone
• mobile
• e-mail
• adress
Nice to have
• inovative design (technology directed)

```html
<!DOCTYPE html>
<html lang="en">
<head>
<meta charset="utf-8">
<title>Tavenorix Technologies – Business Card</title>
<link rel="stylesheet" href="https://fonts.googleapis.com/css2?family=Open+Sans:ital,wght@0,300;0,400;0,700;1,400&display=swap">
<style>
  :root {
    --stage: #d9d9d9;
    --card-white: #f4f4f2;
    --brand-blue: #1a93d3;
    --brand-blue-deep: #1283c4;
    --text-blue: #1d86c6;
    --on-blue: #ffffff;
  }
  * { margin: 0; padding: 0; box-sizing: border-box; }
  html, body { width: 1200px; height: 900px; overflow: hidden; }
  body {
    background: var(--stage);
    font-family: "Open Sans", sans-serif;
    display: flex;
    align-items: center;
    justify-content: center;
    gap: 60px;
  }
  .card {
    width: 510px;
    height: 290px;
    position: relative;
    overflow: hidden;
  }
  .card-front { background: var(--card-white); }
  .card-back { background: var(--brand-blue); }

  .pattern-zone { position: absolute; display: block; }
  .pattern-zone--left { left: 0; top: 0; width: 160px; height: 290px; }
  .pattern-zone--right { right: 0; top: 120px; width: 150px; height: 170px; }

  .contact {
    position: absolute;
    left: 175px;
    top: 62px;
    color: var(--text-blue);
  }
  .contact-name { font-size: 17px; font-weight: 700; letter-spacing: 0.2px; }
  .contact-role { font-size: 12px; font-style: italic; margin-bottom: 14px; }
  .contact-row {
    display: flex;
    align-items: flex-start;
    gap: 9px;
    font-size: 11px;
    line-height: 1.4;
    margin-bottom: 7px;
  }
  .contact-row svg { flex: 0 0 14px; width: 14px; height: 14px; margin-top: 1px; fill: var(--text-blue); }

  .brand {
    position: absolute;
    inset: 0;
    display: flex;
    align-items: center;
    justify-content: center;
    gap: 18px;
    color: var(--on-blue);
  }
  .brand-dot { width: 64px; height: 64px; border-radius: 50%; background: var(--on-blue); }
  .brand-name { font-weight: 300; line-height: 1.1; }
  .brand-name .brand-word { display: block; font-size: 44px; letter-spacing: 1px; }
  .brand-name .brand-sub { display: block; font-size: 12px; letter-spacing: 9px; margin-top: 4px; }
</style>
</head>
<body>

  <section class="card card-front" aria-label="Business card front">
    <svg class="pattern-zone pattern-zone--left" role="img" aria-label="Decorative interlaced blue arc pattern" viewBox="0 0 160 290" preserveAspectRatio="none">
      <defs>
        <linearGradient id="patternFadeLeft" x1="0" y1="0" x2="1" y2="0">
          <stop offset="0" stop-color="#1a93d3" stop-opacity="0.75"/>
          <stop offset="1" stop-color="#1a93d3" stop-opacity="0"/>
        </linearGradient>
      </defs>
      <rect width="160" height="290" fill="url(#patternFadeLeft)"/>
    </svg>
    <svg class="pattern-zone pattern-zone--right" role="img" aria-label="Decorative interlaced blue arc pattern" viewBox="0 0 150 170" preserveAspectRatio="none">
      <defs>
        <linearGradient id="patternFadeRight" x1="1" y1="1" x2="0" y2="0">
          <stop offset="0" stop-color="#1a93d3" stop-opacity="0.75"/>
          <stop offset="1" stop-color="#1a93d3" stop-opacity="0"/>
        </linearGradient>
      </defs>
      <rect width="150" height="170" fill="url(#patternFadeRight)"/>
    </svg>

    <div class="contact">
      <p class="contact-name">Marko L. Varen.</p>
      <p class="contact-role">Director</p>
      <div class="contact-row">
        <svg viewBox="0 0 16 16" aria-hidden="true"><path d="M8 0a8 8 0 1 0 0 16A8 8 0 0 0 8 0zm0 1.4a6.6 6.6 0 1 1 0 13.2A6.6 6.6 0 0 1 8 1.4zM5.6 4c-.4 0-.9.5-.9 1.2 0 2.9 3.2 6.1 6 6.1.7 0 1.1-.5 1.1-.9l-.1-.8-1.6-.7-.8.8c-1-.4-2-1.4-2.4-2.4l.8-.8-.7-1.6z"/></svg>
        <span>+385(0) 52 417 903<br>+385(0) 52 417 903</span>
      </div>
      <div class="contact-row">
        <svg viewBox="0 0 16 16" aria-hidden="true"><path d="M1 3h14v10H1zM2.2 4.2v.3L8 8.6l5.8-4.1v-.3zM2.2 6v5.8h11.6V6L8 10.1z"/></svg>
        <span>info@tavenorix.eu</span>
      </div>
      <div class="contact-row">
        <svg viewBox="0 0 16 16" aria-hidden="true"><path d="M8 0a5.5 5.5 0 0 0-5.5 5.5C2.5 9.6 8 16 8 16s5.5-6.4 5.5-10.5A5.5 5.5 0 0 0 8 0zm0 3.2a2.3 2.3 0 1 1 0 4.6 2.3 2.3 0 0 1 0-4.6z"/></svg>
        <span>72-80 Harlow Lane<br>London N4 2QT<br>United Kingdom</span>
      </div>
    </div>
  </section>

  <section class="card card-back" aria-label="Business card back">
    <div class="brand">
      <span class="brand-dot" aria-hidden="true"></span>
      <p class="brand-name">
        <span class="brand-word">TAVENORIX</span>
        <span class="brand-sub">TECHNOLOGIES</span>
      </p>
    </div>
  </section>

</body>
</html>
```